This is for a poster that will be hanging in the window of a Men's Suit Store in the mall:
Size 4 feet wide by 6 feet high
Main point is: A sale on "Suits" or "Men's Suits" at 40%-60% off ( the 40%-60% off should be the focal point)
Some words that can be used are "Sale" or "Clearance Sale"
Some key words that can be used to make it urgent are "limited time offer" or something similar.
You can get creative, the point is for the customer to want to come into the store and buy a suit right away.
You may use a graphic (picture of a man in a suit). It is not necessary but if it looks good you can use it. (If you do use a picture, it should be of a modern fit or slim fit suit)
Sorry, the initial brief somehow got deleted from the project. Please see the updated brief.
Thanks
Reason: Project was closed for some reason, extended to give enough time to complete
Target Market(s)
Mostly Men ages 35-55
Industry/Entity Type
Store
Colors
Designer to choose colors to be used in the design.

```html
<!DOCTYPE html>
<html lang="en">
<head>
<meta charset="utf-8">
<title>Men's Suits Sale Poster</title>
<link rel="stylesheet" href="https://fonts.googleapis.com/css2?family=Arimo:wght@400;700&display=swap">
<style>
  :root {
    --paper: #ffffff;
    --denim-light: #f2f4f8;
    --denim-mid: #b6c2d8;
    --denim-deep: #7f93b6;
    --navy: #0c0f5e;
    --sale-red: #ff2600;
    --ink: #000000;
    --tag-text: #ffffff;
  }
  html, body {
    margin: 0;
    padding: 0;
    width: 816px;
    height: 1200px;
    overflow: hidden;
    background: var(--paper);
  }
  .poster {
    display: block;
    width: 816px;
    height: 1200px;
    font-family: "Arimo", Arial, sans-serif;
  }
  .headline {
    fill: var(--navy);
    font-size: 86px;
    font-weight: 400;
  }
  .sale-word {
    fill: var(--sale-red);
    font-size: 222px;
    font-weight: 400;
    filter: drop-shadow(2px 3px 2px rgba(0,0,0,0.35));
  }
  .discount {
    fill: var(--ink);
    font-size: 335px;
    font-weight: 700;
    filter: drop-shadow(0 0 6px rgba(255,255,255,0.8));
  }
  .off-word {
    fill: var(--ink);
    font-size: 205px;
    font-weight: 700;
  }
  .tag-shape { fill: var(--sale-red); }
  .tag-hole { fill: var(--tag-text); }
  .tag-line-main {
    fill: var(--tag-text);
    font-size: 80px;
    font-weight: 400;
  }
  .tag-line-sub {
    fill: var(--tag-text);
    font-size: 58px;
    font-weight: 400;
  }
</style>
</head>
<body>
<svg class="poster" viewBox="0 0 816 1200" xmlns="http://www.w3.org/2000/svg">
  <defs>
    <radialGradient id="denimGlow" cx="0.5" cy="0.47" r="0.62">
      <stop offset="0" stop-color="var(--denim-light)" style="stop-color:#f2f4f8"/>
      <stop offset="0.45" stop-color="#b6c2d8"/>
      <stop offset="1" stop-color="#7f93b6"/>
    </radialGradient>
  </defs>

  <rect class="denim-field" x="30" y="32" width="758" height="1138" fill="url(#denimGlow)" role="img" aria-label="Blue denim fabric texture background"/>

  <text class="headline" x="96" y="215" textLength="640" lengthAdjust="spacingAndGlyphs">Men's Suits at</text>

  <text class="sale-word" transform="translate(225,792) rotate(-90)" textLength="502" lengthAdjust="spacingAndGlyphs">SALE</text>

  <text class="discount" x="250" y="530" textLength="522" lengthAdjust="spacingAndGlyphs">40%</text>
  <text class="discount" x="250" y="820" textLength="522" lengthAdjust="spacingAndGlyphs">60%</text>

  <text class="off-word" transform="translate(592,850) rotate(90)" textLength="212" lengthAdjust="spacingAndGlyphs">off</text>

  <g class="offer-tag">
    <polygon class="tag-shape" points="65,845 440,845 550,950 440,1055 65,1055"/>
    <circle class="tag-hole" cx="488" cy="951" r="12"/>
    <text class="tag-line-main" x="80" y="942" textLength="360" lengthAdjust="spacingAndGlyphs">Limited</text>
    <text class="tag-line-sub" x="84" y="1030" textLength="356" lengthAdjust="spacingAndGlyphs">time offer</text>
  </g>
</svg>
</body>
</html>
```